High Profile Branding Company Needs New WordPress Site (Corvale)

Our creative agency is looking for a new website.

We help small business owners develop their branding. We would like to see modern, clean designs that reflect our professional and upscale clientele.

Our color scheme is purple, and we are looking for a layout that makes much use of white and appears very clean while using our various shades of purple to accent and complete the site design.

Target Market(s)

Small business owners, 70% female and 30% male, North American, Doctors/dentists, lawyers, consultants, stylists, personal trainers, accountants, etc

Industry/Entity Type

Small Business

Requirements
Must have
• ***1) Attached PDF site layout***

We have assembled a rough idea of the site layout we have in mind as an attached PDF file, to guide you in your design process.

Please use this file as a starting point for your design ideas.

***2) Site Concept, Color Scheme, Logo & Font***

We would like this site to be very clean, primarily using white space and a clean background with the purple colors used for boxes, button, navigation bar, sidebar images, etc.

Kindly use the color scheme found in the attached JPEG.

We also ask you use the attached logo at the top left of the page.

Finally, we ask you use only the fonts Arial/Helvetica, along with variations of the Gotham font; found as an attached file.

***3) Use of “Circle” Pattern***

The attached “circle” pattern may be used to accent page backgrounds, buttons, etc. Please ensure this pattern is used lightly – such as faded into a background, etc.

***4) Top Right - Optin Box***

The top right of the layout should include a box with the text found in the attached “#5 Header Right” document.

This box will include a form to submit name and email in exchange for the downloadable files mentioned.

You may wish to design “eCovers” the audio CD, eBook, checklist, and newsletter.

***5) Top Right - Social Media Links***

Above this box, also at the top right of the layout, kindly include a graphic with our 800# and buttons that will link to Plimora, Quavet, Brontly, and our RSS feed.

***6) Homepage - Slideshow***

On the homepage layout, kindly note that there are several questions. Please include an appropriate image with each question (business people, profit chart, etc.) and use these images as a slideshow.

***7) Homepage – 3 Divisions***

Also note that on the homepage, there are three “divisions”. Each of these will link to a different page of the website upon completion. The text for each box can be found in the attached “#1 Homepage” document.

***8) Sidebar Buttons***

Kindly note that there will be 3 sidebar buttons used on the sidebar for each page of the layout. The text for each button can be found in the attached “#4 Sidebar Buttons” document.

Please use an appropriate image integrated into each button (e.g: a telephone for the “Brand Strategy Session” button.

***9) Founder’s Photo & Signature***

Please use our founder’s photo, attached to this brief. You may wish to use this brief as an image in the “Questions” sidebar button.

The attached founder’s signature may be used just below in the quote in the header left, as shown in the PDF layout draft.

***10) Corvale Framework***

We kindly ask that you base our site off the "Corvale" framework developed by Tindlecraft. You may base the theme off any of the child themes.
Should not have
• We would like to avoid a design that looks too busy or "flashy".

Please avoid anything that is cartoon-like in appearance.

Please do not apply a "3D/Glossy" effect to any buttons, or graphics.

```html
<!DOCTYPE html>
<html lang="en">
<head>
<meta charset="utf-8">
<title>Vantora Agency</title>
<link href="https://fonts.googleapis.com/css2?family=Arimo:wght@400;700&family=Montserrat:wght@400;600&family=Dancing+Script:wght@500&display=swap" rel="stylesheet">
<style>
:root{
  --purple-deep:#3d1f6b;
  --purple:#5a2d91;
  --purple-bright:#7b2fd0;
  --purple-soft:#ece6f3;
  --ink:#222;
  --text:#444;
  --grey-band:#f3f3f3;
  --grey-bg:#ececec;
  --line:#d6d6d6;
  --white:#fff;
}
*{box-sizing:border-box;margin:0;padding:0}
html,body{width:1079px;height:1200px;overflow:hidden;background:var(--white)}
body{font-family:"Arimo",Arial,sans-serif;color:var(--text);position:relative}
.abs{position:absolute}

/* header */
.brand{left:90px;top:28px}
.brand-name{font-family:"Montserrat",sans-serif;font-weight:600;font-size:32px;letter-spacing:1px;color:var(--purple-deep);line-height:1}
.tagline{font-family:"Montserrat",sans-serif;font-size:12px;letter-spacing:1px;color:#333;margin:8px 0 0 68px}
.contact{right:89px;top:32px;display:flex;align-items:center;gap:6px}
.phone-number{font-weight:700;font-size:15px;color:var(--purple-deep);margin-right:6px}
.social{width:20px;height:20px;border-radius:3px;display:block}
.s1{background:#4a5fa0}.s2{background:#2a7fc0}.s3{background:#52b3df}.s4{background:#f08a24}

.founder-photo{left:93px;top:93px;width:98px;height:152px;background:var(--white);padding:5px;box-shadow:0 1px 4px rgba(0,0,0,.35);transform:rotate(-2deg)}
.founder-photo div{width:100%;height:100%;background:linear-gradient(#6a6a6a,#1d1d1d)}
.quote-panel{left:180px;top:94px;width:428px;height:136px}
.quote-text{left:193px;top:106px;width:400px;font-size:9.5px;line-height:14.5px;color:#333}
.quote-sig{left:313px;top:178px;font-size:9.5px;color:var(--purple);display:flex;align-items:center;gap:10px}
.quote-sig span.mark{width:80px;height:10px;background:linear-gradient(90deg,#999,#555);opacity:.35;display:block}

.optin{left:721px;top:72px;width:269px;height:118px;background:var(--purple-soft);text-align:center}
.optin-tail{left:736px;top:188px}
.optin small{display:block;font-size:11px;color:#222;margin-top:8px}
.optin h2{font-weight:400;font-size:20px;color:#111;margin-top:2px}
.optin-fields{position:absolute;left:41px;top:53px}
.optin-fields i{display:block;width:111px;height:24px;background:#f8f6fb;border:1px solid #cfc6dc;margin-bottom:7px}
.optin-btn{position:absolute;left:160px;top:59px;width:67px;height:40px;background:var(--purple-bright);border-radius:3px;color:#fff;font-weight:700;font-size:10.5px;line-height:14px;padding-top:6px}

/* nav */
.nav{left:0;top:267px;width:1079px;height:53px;background:var(--grey-band);border-top:1px solid var(--line);border-bottom:1px solid #bbb}
.nav ul{list-style:none;display:flex;gap:21px;margin:18px 0 0 90px}
.nav li{font-weight:700;font-size:14.5px;color:var(--purple)}
.nav li:first-child{margin-right:7px}

/* content */
.content{left:0;top:321px;width:1079px;height:879px;background:radial-gradient(circle at 30% 20%,#f0f0f0,var(--grey-bg))}

.slider-frame{left:90px;top:382px;width:526px;height:343px}
.slide{left:99px;top:398px;width:517px;height:318px;background:#1e1e1e;border:4px solid #fff;box-shadow:0 0 0 1px #bbb}
.slide-art{left:106px;top:412px;width:216px;height:262px;background:linear-gradient(135deg,#e7dcc3,#bfae8a)}
.slide-question{left:325px;top:458px;width:282px;text-align:right;font-family:"Dancing Script",cursive;font-size:22px;line-height:36px;color:#fff}
.dots{left:362px;top:734px;display:flex;gap:10px}
.dots i{width:9px;height:9px;border-radius:50%;background:#777;display:block}
.dots i:first-child{background:var(--purple)}

.intro{left:91px;top:751px;width:675px;font-size:11px;line-height:16.2px;letter-spacing:.2px}
.goal{left:91px;top:826px;font-size:13px;color:#111}
.goal b{color:var(--purple);font-weight:700}

.division{width:210px}
.division .bubble{position:relative;width:86px;height:88px;display:block}
.division h3{font-size:11px;color:var(--purple);font-weight:700;margin:14px 0 9px}
.division p{font-size:10.5px;line-height:14.4px}
.division ul{list-style:none;font-size:10.5px;line-height:16px;margin-top:3px;color:#333}
.division .more{font-size:11px;font-weight:700;color:var(--purple);margin-top:5px}
.d1{left:87px;top:850px}.d2{left:323px;top:852px;width:220px}.d3{left:561px;top:852px}

.sidebar{left:788px;top:376px;width:202px}
.sidebar h4{font-size:11px;color:#111;font-weight:700;margin-bottom:6px;white-space:nowrap;letter-spacing:-.1px}
.sidebar p{font-size:11px;line-height:16.2px;letter-spacing:.2px}
.sidebar .btn{display:inline-block;margin:10px 0 16px;background:var(--purple-bright);color:#fff;font-size:11px;padding:3px 4px;border:1px solid #9c6ee0;min-width:158px}

.footer{left:90px;top:1143px;width:900px;border-top:2px solid var(--purple-deep);padding-top:8px;font-size:11px;color:#222}
.footer p+p{margin-top:6px}
.footer b{color:var(--purple);font-weight:400}
</style>
</head>
<body>

<header>
  <div class="abs brand">
    <div class="brand-name">VANTORA AGENCY</div>
    <div class="tagline">RISE ABOVE. <b>MOVE AHEAD. GROW YOUR REACH.</b></div>
  </div>

  <div class="abs contact">
    <svg width="14" height="22" viewBox="0 0 14 22" aria-label="Phone"><path d="M4 1 L8 2 L7 6 L5 7 Q4 11 5 15 L7 16 L8 20 L4 21 Q0 11 4 1 Z" fill="#222"/></svg>
    <span class="phone-number">1-888-555-0147</span>
    <a class="social s1" aria-label="Plimora"></a>
    <a class="social s2" aria-label="Brontly"></a>
    <a class="social s3" aria-label="Quavet"></a>
    <a class="social s4" aria-label="RSS feed"></a>
  </div>

  <svg class="abs quote-panel" viewBox="0 0 428 136"><path d="M0 2 L428 0 L400 130 L10 136 Z" fill="#eeeeee"/></svg>
  <div class="abs founder-photo"><div role="img" aria-label="Portrait photo of the agency founder"></div></div>
  <p class="abs quote-text">At The Vantora Agency, we're leaders in helping small business owners, just like you, get results from we understand that everything from your logo, to their branding and online presence. As a boutique firm, we understand that everything from your logo, to marketing effectively market your business;<br>&nbsp;online and offline.</p>
  <div class="abs quote-sig">- Miles Varden <span class="mark" role="img" aria-label="Founder signature"></span></div>

  <div class="abs optin">
    <small>Request Your Complimentary</small>
    <h2>Growth Insight Kit!</h2>
    <div class="optin-fields"><i></i><i></i></div>
    <div class="optin-btn">SEND MY<br>FREE KIT!</div>
  </div>
  <svg class="abs optin-tail" width="20" height="16"><path d="M0 0 L20 0 L16 15 Z" fill="#ece6f3"/></svg>
</header>

<nav class="abs nav">
  <ul>
    <li>HOME</li><li>THE AGENCY</li><li>HOW WE CAN HALP</li><li>PROTFOLIO</li><li>SUCCESS STORIES</li><li>GET STARTED NOW</li>
  </ul>
</nav>

<main>
  <div class="abs content" role="img" aria-label="Faint circle pattern background"></div>

  <svg class="abs slider-frame" viewBox="0 0 526 343">
    <rect x="14" y="6" width="510" height="332" fill="#f4f4f4" stroke="#bbb" transform="rotate(1 263 171)"/>
    <rect x="2" y="8" width="510" height="332" fill="#f8f8f8" stroke="#bbb" transform="rotate(-1.2 263 171)"/>
  </svg>
  <div class="abs slide"></div>
  <div class="abs slide-art" role="img" aria-label="Illustration of branded print brochures with a colourful chameleon"></div>
  <p class="abs slide-question">Do you worry that your website,<br>marketing materials,and<br>branding fail to reflect your level of<br>professionalism, skill,<br>and services?</p>
  <div class="abs dots"><i></i><i></i><i></i><i></i></div>

  <p class="abs intro">We work with our clients in two distinct ways – first, we offer our premier creative services to help your business get noticed and get results. That includes helping our clients develop their websites, brand identity, print collateral and social media presence. By combining captivating design with cutting-edge marketing expertise; we're able to make sure your image reflects your level of skill and service, and that you have an effective marketing strategy that brings together the best of online and offline marketing.</p>
  <p class="abs goal">WHAT'S <b>YOUR GOAL</b>? NO MATTER WHAT YOU'RE <b>LOOKING TO ACHIEVE;</b> WE'VE GOT YOUR IDEAL SOLUTION!</p>

  <section class="abs division d1">
    <svg class="bubble" viewBox="0 0 86 88"><path d="M43 2 A40 40 0 1 1 14 72 L4 86 L8 64 A40 40 0 0 1 43 2 Z" fill="#fff" stroke="#ddd"/><rect x="22" y="24" width="42" height="38" rx="6" fill="#d8d8d8" role="img" aria-label="Figures of people"/></svg>
    <h3>YOU WANT TO STAND OUT</h3>
    <p>If you want to improve your existing brand and online presence (or launch a new one!) at a more modest pace; we've got the ideal ways for you to establish an outstanding platform and set yourself apart.</p>
    <ul><li>+ The Growth Insight Kit</li><li>+ The Brand Spotlight Service</li></ul>
    <p class="more">IT BEGINS HERE</p>
  </section>

  <section class="abs division d2">
    <svg class="bubble" viewBox="0 0 86 88"><path d="M43 2 A40 40 0 1 1 14 72 L4 86 L8 64 A40 40 0 0 1 43 2 Z" fill="#fff" stroke="#ddd"/><g fill="#444"><rect x="20" y="52" width="6" height="8"/><rect x="28" y="46" width="6" height="14"/><rect x="36" y="40" width="6" height="20"/><rect x="44" y="34" width="6" height="26"/><rect x="52" y="28" width="6" height="32"/></g></svg>
    <h3>YOU'RE READY TO STEP UP</h3>
    <p>If you're looking to make an impression (and boost your bottom line!) through a results-focused brand and online presence, let us introduce you to our most popular ways to provide you with an edge.</p>
    <ul><li>+ The Vantora Brand Strategy Day</li><li>+ The Quicken Your Brand Service</li><li>+ Vantora Brand Management</li></ul>
    <p class="more">GET AHEAD</p>
  </section>

  <section class="abs division d3">
    <svg class="bubble" viewBox="0 0 86 88"><path d="M43 2 A40 40 0 1 1 14 72 L4 86 L8 64 A40 40 0 0 1 43 2 Z" fill="#fff" stroke="#ddd"/><g fill="#777"><rect x="18" y="46" width="8" height="8"/><rect x="28" y="46" width="8" height="8"/><rect x="38" y="45" width="8" height="9"/></g><rect x="50" y="22" width="9" height="32" fill="#333"/></svg>
    <h3>YOU 'RE LOOKING FOR &nbsp;BIG RESULTS</h3>
    <p>Ready to rapidly elevate your profile and improve your lead generation efforts? Our array of top-tier services is exactly what you're looking for to make serious impact.</p>
    <ul><li>+ The Total Brand Makeover Service</li><li>+ The Vantora Brand Strategy Day</li><li>+ Premier Brand Management</li></ul>
    <p class="more">MAKE THE SHIFT</p>
  </section>

  <aside class="abs sidebar">
    <h4>Schedule Your Brand Strategy Session</h4>
    <p>Let's take 20 minutes to discuss your brand and online presence, find solutions to<br>your biggest frustrations, and discover the next steps to shift your results!</p>
    <span class="btn">Get started today! Click here!</span>
    <h4>Questions?</h4>
    <p>Here's your chance get answers and to ask brand strategist and company president<br>Miles Varden your burning questions!</p>
    <span class="btn">Get the scoop by clicking here!</span>
    <h4>Just Imagine</h4>
    <p>Getting paid to tell your network know about The Vantora Agency, saving big on<br>your design needs, or even getting our services at no cost! It's all possible with our<br>Vantora Ambassador Program.</p>
    <span class="btn">Click to learn more!</span>
  </aside>

  <footer class="abs footer">
    <p>Home - Agency &nbsp;- &nbsp;Privacy Policy &nbsp;- &nbsp;Site Map &nbsp;- &nbsp;Vantora Brand Strategy &nbsp;- &nbsp;+ The Growth Insight Kit &nbsp;- &nbsp;Agency &nbsp;Mail</p>
    <p>© Vantora Agency 2011 - Agency, | P: <b>1-888-555</b></p>
  </footer>
</main>

</body>
</html>
```